Fast Money - Simple Book Cover Design

Hello,

I am in need of a cover for my new book. The Book Title Is

"Standing Growth - Keys to Glowing Customer Ratings That Fill The Calendar and Draw Fresh Clients Through Every Entrance!"

Author: Fireman Dale Orsworth

What I want: This is a book for businesses on improving their online reputation. I want to have 5 Stars on the cover. You can look at this quarvex search for ideas of what I am meaning.....

(copy and paste)

http://www.quarvex-find.example/search?q=5+star+online+reviews&mode=images&ref=kx7Lp2QwZt9 (copy and paste)

I am open to different color schemes for the book. I am partial to dark blues if you make it look good. Here is another book that I really like the cover of....

http://www.brindlemart.example/Clipwave-Tactics-Earning-Promotion-ebook/item/Z93KT4WQPX

I want the cover BOLD and to STAND OUT.

I am looking for a design to help establish me as an authority for online reputation marketing. This book will be both in Pagely format and be used in print as well.

I am open to questions....

Thanks!

Dale

Reason: I don't believe we have received the right designs. I am going to give everyone more time...

Reason: Hi everyone, I had some stuff come up and was not able to be involved in this project. I am extending because we have not seen the exact thing we want and need time to work with designers to get it right. Thanks Dale

Reason: I am currently traveling and can't wrap this up until I get back.

Target Market(s)

Business Owners

Industry/Entity Type

Business

Requirements
Must have
• Title and Subtitle

Author Name

5 Stars Images....
Nice to have
• Creativity

Bold and stand out

Professional

Should not have
• thin text, small to read text, lame graphics,

```html
<!DOCTYPE html>
<html lang="en">
<head>
<meta charset="utf-8">
<title>Standing Growth — Book Cover</title>
<link rel="stylesheet" href="https://fonts.googleapis.com/css2?family=Oswald:wght@500;700&family=Arimo:wght@700&family=Archivo+Narrow:wght@500&display=swap">
<style>
  :root {
    --navy-deep: #05082e;
    --navy: #0c1466;
    --royal: #1f2fb8;
    --title-white: #ffffff;
    --subtitle-cream: #fff6dc;
    --author-grey: #d9dbe8;
    --gold-light: #ffe39a;
    --gold: #e0a93a;
    --gold-dark: #9a6414;
  }
  html, body {
    margin: 0;
    padding: 0;
    width: 814px;
    height: 1200px;
    overflow: hidden;
    background: var(--navy-deep);
  }
  .cover {
    position: relative;
    width: 814px;
    height: 1200px;
    overflow: hidden;
  }
  .cover-backdrop {
    position: absolute;
    inset: 0;
    background:
      radial-gradient(ellipse 70% 55% at 55% 45%, var(--royal) 0%, var(--navy) 45%, var(--navy-deep) 100%);
  }
  .title-art {
    position: absolute;
    left: 0;
    top: 0;
    width: 814px;
    height: 360px;
  }
  .title-main {
    font-family: "Oswald", "Arial Narrow", sans-serif;
    font-weight: 700;
    fill: var(--title-white);
  }
  .title-second {
    font-family: "Oswald", "Arial Narrow", sans-serif;
    font-weight: 500;
    fill: var(--title-white);
  }
  .subtitle {
    position: absolute;
    left: 0;
    right: 0;
    top: 395px;
    margin: 0;
    text-align: center;
    font-family: "Arimo", Arial, sans-serif;
    font-weight: 700;
    font-size: 41px;
    line-height: 49px;
    color: var(--subtitle-cream);
    letter-spacing: 0.5px;
  }
  .subtitle span { display: block; }
  .rating-stars {
    position: absolute;
    left: 60px;
    top: 905px;
    width: 694px;
    height: 120px;
  }
  .author {
    position: absolute;
    left: 0;
    right: 0;
    top: 1085px;
    margin: 0;
    text-align: center;
    font-family: "Archivo Narrow", "Arial Narrow", sans-serif;
    font-weight: 500;
    font-size: 36px;
    letter-spacing: 2px;
    word-spacing: 14px;
    color: var(--author-grey);
  }
</style>
</head>
<body>
  <main class="cover">
    <div class="cover-backdrop" role="img" aria-label="Dark blue background of overlapping translucent squares glowing brighter toward the centre"></div>

    <svg class="title-art" viewBox="0 0 814 360" aria-label="Standing Growth">
      <text class="title-main" x="45" y="203" textLength="724" lengthAdjust="spacingAndGlyphs"><tspan font-size="190">S</tspan><tspan font-size="158">TANDING</tspan></text>
      <text class="title-second" x="105" y="322" font-size="120" textLength="610" lengthAdjust="spacing">GROWTH</text>
    </svg>

    <p class="subtitle">
      <span>Keys to Glowing</span>
      <span>Customer Ratings</span>
      <span>That Fill The Calendar</span>
      <span>and Draw Fresh Clients</span>
      <span>Through Every Entrance!</span>
    </p>

    <svg class="rating-stars" viewBox="0 0 694 120" aria-label="Five gold stars">
      <defs>
        <linearGradient id="starGold" x1="0" y1="0" x2="0.6" y2="1">
          <stop offset="0" stop-color="var(--gold-light)"/>
          <stop offset="0.5" stop-color="var(--gold)"/>
          <stop offset="1" stop-color="var(--gold-dark)"/>
        </linearGradient>
        <polygon id="star" points="0,-52 12.2,-16.8 49.5,-16.1 19.8,6.4 30.6,42.1 0,20.8 -30.6,42.1 -19.8,6.4 -49.5,-16.1 -12.2,-16.8" fill="url(#starGold)" stroke="var(--gold-dark)" stroke-width="2" stroke-linejoin="round"/>
      </defs>
      <use href="#star" x="64" y="60"/>
      <use href="#star" x="205" y="60"/>
      <use href="#star" x="347" y="60"/>
      <use href="#star" x="486" y="60"/>
      <use href="#star" x="624" y="60"/>
    </svg>

    <p class="author">Fireman Dale Orsworth</p>
  </main>
</body>
</html>
```